Header Needed For Whimsical, Historical Book Blog

Gather Every Volume! (https://mkplovane.quillpage.example/) is a book blog that specializes in book reviews, book lists, and literature discussions. It badly needs a new header.

- The majority of the books that get featured on the blog involve nature or history. It would be helpful if the new header incorporated the Victorian era, nature, and books.

- The blog’s name (Gather Every Volume!) must be in the header. My name (MK Plovane) must also be in the header. The blog’s name is much more important than mine.

- The current header is 1168 X 220. The new header can be bigger, smaller, or the same size. There is an advertisement in the blog’s right sidebar. That ad must be *partially* visible without scrolling. (The top part of the ad must be “above the fold.”) The header can’t be so big that people need to scroll to see the ad.

- The header should not be more than 1600 wide. If it's wider than 1600, Pagewright will crop it.

- JPEG or PNG.

- Books! When people visit the blog, they must know immediately that they’re looking at a book blog.

- The blog’s current logo is a black top hat and a book. The logo will probably change eventually.

- The whole blog will be getting a makeover, so the header can be any color and use any font. The blog’s new design will hopefully be inspired by the header.

- The blog posts will most likely have black or gray text on a white background. The header should look nice on a site that’s mostly white / light colored.

- The books featured on the blog are serious, but the tone of the posts is often humorous. The blog’s readers love whimsy, forests, old books, and gentleman animals. I’m looking for a header that will grab people’s attention and make them smile. I want something quirky and memorable.

Good luck! Thank you for your help. I’m looking forward to seeing your designs.

Target Market(s)

Bookworms. Most of the current audience is women ages 25-34.

Colors

Designer to choose colors to be used in the design.

Requirements
Must have
• - "Gather Every Volume!" and "MK Plovane" written in the header.
• - The ad in the blog's right sidebar must be partially visible without scrolling.
• - Books! Readers must know that this is a book blog.
• - JPEG or PNG.
Nice to have
• - The Victorian era and nature.
• - Top hats.
• - A header that looks good on a mostly white blog.
Should not have
• - Anything that makes Gather Every Volume! look too much like other book blogs. Other blogs' headers tend to have pastel colors, flowers, and coffee/tea cups. I’m not completely opposed to those things, but I’d prefer to go in a different direction.
• - The header should not be more than 1600 wide. If it is, Pagewright will crop it.

```html
<!DOCTYPE html>
<html lang="en">
<head>
<meta charset="utf-8">
<title>Gather Every Volume! — The Sunday Post #207</title>
<link href="https://fonts.googleapis.com/css2?family=Archivo+Black&family=Rye&family=Dancing+Script:wght@500&family=Caveat:wght@500&family=Roboto:wght@400&display=swap" rel="stylesheet">
<style>
  :root {
    --paper: #ebe7e1;
    --paper-light: #f4f2ee;
    --shell: rgba(250,249,247,0.75);
    --header-bg: #f1f1f0;
    --ink: #111111;
    --accent-red: #d7261b;
    --wine: #7a1509;
    --nav-red: #8b1a10;
    --rule: #d6d3ce;
    --post-border: #5a5a5a;
    --ad-text: #555555;
    --ad-muted: #a0a0a0;
  }
  * { margin: 0; padding: 0; box-sizing: border-box; }
  html, body { width: 1200px; height: 617px; overflow: hidden; }
  body {
    position: relative;
    background: radial-gradient(ellipse at 30% 40%, var(--paper-light), var(--paper) 70%);
    font-family: "Roboto", sans-serif;
  }
  .note {
    position: absolute; top: 9px; left: 0; width: 1156px; text-align: center;
    font-family: "Archivo Black", sans-serif; font-size: 14.5px; letter-spacing: 0.6px;
    color: var(--accent-red);
  }
  .shell {
    position: absolute; left: 145px; top: 20px; width: 898px; height: 620px;
    background: var(--shell); border: 1px solid #e2dfda; border-radius: 8px;
  }
  .masthead {
    position: absolute; left: 172px; top: 31px; width: 845px; height: 159px;
    background: var(--header-bg); border-radius: 6px;
    box-shadow: 0 1px 3px rgba(0,0,0,0.25);
    overflow: hidden;
  }
  .masthead-title {
    position: absolute; font-family: "Rye", serif; font-weight: 400; color: var(--ink);
    line-height: 1; white-space: nowrap;
  }
  .title-left { left: 38px; top: 50px; font-size: 54px; }
  .title-right { left: 532px; top: 55px; font-size: 39px; }
  .emblem { position: absolute; left: 329px; top: 19px; }
  .byline {
    position: absolute; left: 698px; top: 128px;
    font-family: "Archivo Black", sans-serif; font-size: 12px; letter-spacing: 0.6px; color: var(--ink);
  }
  .nav {
    position: absolute; left: 156px; top: 196px; width: 877px; height: 36px;
    border-top: 1px solid var(--rule); border-radius: 0 0 8px 8px;
    background: linear-gradient(#ffffff, #ecebea);
  }
  .nav ul { list-style: none; position: absolute; left: 0; top: 0; height: 36px; }
  .nav li {
    position: absolute; top: 0; height: 36px; line-height: 34px; text-align: center;
    font-family: "Dancing Script", cursive; font-size: 16px; color: var(--nav-red);
    border-right: 1px solid var(--rule); white-space: nowrap;
  }
  .nav li.current { color: var(--ink); }
  .date, .sidebar-heading {
    position: absolute; top: 246px;
    font-family: "Caveat", cursive; font-weight: 500; font-size: 17px; color: var(--ink); letter-spacing: 0.3px;
    text-transform: uppercase; white-space: nowrap;
  }
  .date { left: 169px; }
  .sidebar-heading { left: 803px; }
  .post {
    position: absolute; left: 156px; top: 277px; width: 629px; height: 360px;
    background: #fff; border: 1px solid var(--post-border); border-radius: 6px;
  }
  .post-title {
    position: absolute; left: 0; top: 10px; width: 100%; text-align: center;
    font-family: "Dancing Script", cursive; font-size: 40px; color: var(--wine); font-weight: 500;
  }
  .post-feature {
    position: absolute; left: 219px; top: 87px; width: 192px; height: 280px;
    background: linear-gradient(#ecebe8, #dedbd6);
  }
  .social { position: absolute; left: 807px; top: 277px; }
  .adchoices {
    position: absolute; left: 994px; top: 338px; width: 24px; height: 11px;
    border: 1px solid #aaa; background: #fff;
  }
  .ad-icon { position: absolute; left: 816px; top: 400px; width: 64px; height: 64px; background: #eef1f5; }
  .ad-title {
    position: absolute; left: 893px; top: 394px; width: 120px;
    font-size: 16px; line-height: 19px; color: var(--ad-text);
  }
  .ad-domain { position: absolute; left: 893px; top: 459px; font-size: 7.5px; color: var(--ad-muted); }
  .ad-cta { position: absolute; left: 816px; top: 504px; font-size: 9px; color: var(--ad-text); }
  .ad-photo {
    position: absolute; left: 817px; top: 550px; width: 189px; height: 67px;
    background: linear-gradient(90deg, #6b8a55, #b8557a 35%, #6a5a55 55%, #b0682e 80%, #5fae6a);
  }
</style>
</head>
<body>
  <p class="note">*P.S: COULD BE COLORED TOO*</p>
  <div class="shell"></div>

  <header class="masthead">
    <h1 class="masthead-title title-left">Gather</h1>
    <svg class="emblem" width="188" height="124" viewBox="0 0 188 124" role="img" aria-label="Gentleman in a top hat above a stack of open books">
      <ellipse cx="93" cy="59" rx="92" ry="57" fill="none" stroke="#111" stroke-width="1.5"/>
      <rect x="12" y="2" width="164" height="120" fill="#d9d8d5" rx="40"/>
    </svg>
    <h1 class="masthead-title title-right">Every Volume!</h1>
    <p class="byline">BY: MK PLOVANE</p>
  </header>

  <nav class="nav">
    <ul>
      <li class="current" style="left:188px;width:58px;">Home</li>
      <li style="left:246px;width:88px;">About Me</li>
      <li style="left:334px;width:111px;">Review Policy</li>
      <li style="left:445px;width:139px;">Discussion Library</li>
      <li style="left:584px;width:113px;">Privacy Policy</li>
    </ul>
  </nav>

  <p class="date">Sunday, January 12, 2020</p>

  <article class="post">
    <h2 class="post-title">The Sunday Post #207</h2>
    <div class="post-feature" role="img" aria-label="Weekly feature graphic with a sketched forest creature on parchment"></div>
  </article>

  <p class="sidebar-heading">Stalk me everywhere</p>
  <svg class="social" width="210" height="36" viewBox="0 0 210 36" aria-label="Follow links">
    <g fill="#111">
      <circle cx="17" cy="17" r="16.5"/>
      <circle cx="52" cy="17" r="16.5"/>
      <circle cx="86" cy="17" r="16.5"/>
      <circle cx="121" cy="17" r="16.5"/>
      <circle cx="156" cy="17" r="16.5"/>
      <circle cx="191" cy="17" r="16.5"/>
    </g>
    <g stroke="#fff" stroke-width="2" fill="none">
      <path d="M17 8v18M8 17h18"/>
      <rect x="42" y="11" width="20" height="13" stroke-width="1.5"/>
      <path d="M42 11l10 8 10-8" stroke-width="1.5"/>
    </g>
  </svg>

  <div class="adchoices"></div>
  <div class="ad-icon" role="img" aria-label="Blue paw print icon"></div>
  <p class="ad-title">Top 5 Pup Treat Crates</p>
  <p class="ad-domain">pawcratecompare.example</p>
  <p class="ad-cta">Compare Prices and Subscribe</p>
  <div class="ad-photo" role="img" aria-label="Photo of two treat subscription boxes compared side by side with a dog"></div>
</body>
</html>
```